Braek down, maintainance and support for satelite and TV

I want a website designed for a satellite engineer firm i want it to look modern. I am finalizing the content with the underwriters at the moment so format we can start on the format and pictures. I want it to be easy to navigate with some eye capturing imiges. I am currently waiting for the underwriters to get the contact over so if we can start on everything else. I ONLY ADDED THE SCREEN SHOT AS I HAD TO ADD SOMETHING TO CONTINUE PLEASE USE YOUR OWN IDEAS

Target Market(s)

Every one

Industry/Entity Type

Tv

Number of Pages Required

5+ page

Font styles to use
Sans Serif

```html
<!DOCTYPE html>
<html lang="en">
<head>
<meta charset="utf-8">
<title>Satellite Engineer</title>
<link rel="stylesheet" href="https://fonts.googleapis.com/css2?family=Arimo:wght@400;700&family=Ubuntu+Condensed&display=swap">
<style>
:root{
  --ink:#333;
  --muted:#555;
  --nav:#777;
  --blue:#1a55c8;
  --link:#1a4fbf;
  --band:#e9e9e9;
  --band-dark:#c9cbce;
  --footer:#ececec;
  --line:#d4d4d4;
}
*{box-sizing:border-box;margin:0;padding:0}
html,body{width:860px;height:1200px;overflow:hidden}
body{position:relative;background:#fff;font-family:Arimo,Arial,sans-serif;color:var(--ink)}
.abs{position:absolute}
.site-header{position:absolute;left:0;top:0;width:860px;height:88px;background:#fff}
.brand{left:70px;top:29px;font-family:"Ubuntu Condensed","Arial Narrow",sans-serif;font-size:22px;color:#333;letter-spacing:.2px;white-space:nowrap}
.brand-sub{left:70px;top:69px;font-size:13px;color:#222}
.phone-tab{right:0;top:0;width:200px;height:28px}
.phone-label{right:48px;top:4px;font-size:16px;font-weight:700;color:#c4c4c4}
.nav a{position:absolute;top:50px;font-size:11px;font-weight:700;color:var(--nav);text-decoration:none;letter-spacing:.2px}
.nav .current{left:393px;top:45px;width:58px;height:23px;background:var(--blue);color:#fff;border-radius:4px;border:1px solid #0e3a94;text-align:center;line-height:21px}
.hero{left:0;top:88px;width:860px;height:300px;background:linear-gradient(160deg,#2d6ec0 0%,#5f9ad6 45%,#9ec7ea 100%)}
.features{left:0;top:388px;width:860px;height:110px;background:var(--band);border-bottom:1px solid var(--line)}
.feature-title{font-size:14px;font-weight:700;color:#444}
.feature-text{font-size:11px;color:#555;line-height:14px;margin-top:2px}
.col h2{font-size:22px;font-weight:700;color:#555;margin-bottom:20px}
.col .photo{width:238px;height:127px}
.col p{font-size:11.2px;line-height:18px;color:#444;margin-top:16px;width:232px}
.btn{position:absolute;top:877px;height:24px;padding:0 9px;border:1px solid #bdbdbd;border-radius:3px;background:linear-gradient(#fafafa,#e4e4e4);font-size:11.5px;font-weight:700;color:#666;line-height:22px}
.footer{left:0;top:955px;width:860px;height:190px;background:var(--footer);border-top:2px solid #d8d8d8}
.footer h3{font-size:14px;font-weight:700;color:#555}
.footer ul{list-style:none;font-size:11px;color:#555;line-height:18px}
.testimonial{font-size:10.6px;color:#555;line-height:18px;width:290px}
.post{font-size:10.4px;color:#555;line-height:13px;width:275px}
.post a{color:var(--link);font-weight:700;text-decoration:none;display:block}
.bottom-bar{left:0;top:1145px;width:860px;height:55px;background:var(--footer);border-top:1px solid var(--line)}
.copyright{left:38px;top:1165px;font-size:11px;color:#444}
.social{top:1163px;width:14px;height:14px;border-radius:2px}
</style>
</head>
<body>
<header class="site-header">
  <div class="abs brand">SATELLITE ENGINEER</div>
  <div class="abs brand-sub">(YOUR LOGO)</div>
  <svg class="abs phone-tab" viewBox="0 0 200 28"><path d="M0 0 H200 V28 H40 Q28 28 22 14 Q16 0 0 0Z" fill="#f1f1f1" stroke="#ddd"/><path d="M37 8 q-3 5 2 10 q5 5 9 2 l-2-3 -3 1 q-3-2-4-5 l2-2z" fill="#c8c8c8"/></svg>
  <div class="abs phone-label">PHONE</div>
  <nav class="nav">
    <a class="current" href="#">HOME</a>
    <a href="#" style="left:486px">ABOUT</a>
    <a href="#" style="left:572px">SERVICES</a>
    <a href="#" style="left:673px">OTHER PAGE</a>
    <a href="#" style="left:786px">CONTACT</a>
  </nav>
</header>

<div class="abs hero" role="img" aria-label="Engineers on a lift platform servicing a large satellite dish against a blue sky"></div>

<section class="abs features">
  <svg class="abs" style="left:440px;top:0" width="395" height="21"><path d="M0 0 H395 L375 21 H20Z" fill="var(--band-dark)"/></svg>
  <svg class="abs" style="left:46px;top:34px" width="64" height="56"><rect x="4" y="10" width="54" height="40" rx="8" fill="#c4621a"/><rect x="8" y="14" width="46" height="32" rx="6" fill="#e08535"/><rect x="36" y="22" width="22" height="16" rx="3" fill="#b0510f"/><circle cx="45" cy="30" r="3" fill="#f0c060"/></svg>
  <div class="abs" style="left:125px;top:42px"><div class="feature-title">Save big with us</div><div class="feature-text">Lorem ipsum dolor sit amet,<br>consectetur adipiscing elit.</div></div>
  <svg class="abs" style="left:322px;top:30px" width="60" height="60"><circle cx="30" cy="30" r="28" fill="#e7a21b"/><circle cx="30" cy="30" r="22" fill="#fffbea"/><path d="M30 30 V14 M30 30 L40 34" stroke="#8a4e10" stroke-width="2.5" stroke-linecap="round"/></svg>
  <div class="abs" style="left:393px;top:42px"><div class="feature-title">Always on time</div><div class="feature-text">Lorem ipsum dolor sit amet,<br>consectetur adipiscing elit.</div></div>
  <svg class="abs" style="left:588px;top:34px" width="68" height="56"><path d="M6 34 L46 20 L64 34 L24 50Z" fill="#9fb3c8"/><path d="M6 34 L24 50 V54 L6 38Z" fill="#6f859b"/><path d="M12 16 q22-14 44 0 l-6 8 q-16-8-32 0z" fill="#4d6680"/><rect x="30" y="26" width="16" height="6" fill="#f28a1c" transform="rotate(-18 38 29)"/></svg>
  <div class="abs" style="left:670px;top:42px"><div class="feature-title">Contact Us</div><div class="feature-text">Lorem ipsum dolor sit amet,<br>consectetur adipiscing elit.</div></div>
</section>

<main>
  <article class="abs col" style="left:37px;top:530px">
    <h2>Who we are?</h2>
    <div class="photo" role="img" aria-label="Two business people standing in front of a ground station satellite dish" style="background:linear-gradient(180deg,#6c93c8,#c9d6e6 55%,#5d8a3a 85%)"></div>
    <p>Lorem ipsum dolor sit amet, consectetur adipiscing elit. Etiam tristique tristique lacus in varius. Donec nec vestibulum ligula. Aenean turpis diam, feugiat a luctus in, rhoncus eget risus. Maecenas consequat porttitor dui, vitae consequat massa imperdiet ut. elit ut tempus lobortis, eros leo molestie velit, non egestas augue nulla eget erat.</p>
  </article>
  <article class="abs col" style="left:314px;top:530px">
    <h2>What we do?</h2>
    <div class="photo" role="img" aria-label="Technician working beside a dish mast on a hilltop above forest" style="background:linear-gradient(180deg,#7aa6d8,#b9cde0 40%,#4e6f3b 75%)"></div>
    <p>Lorem ipsum dolor sit amet, consectetur adipiscing elit. Etiam tristique tristique lacus in varius. Donec nec vestibulum ligula. Aenean turpis diam, feugiat a luctus in, rhoncus eget risus. Maecenas consequat porttitor dui, vitae consequat massa imperdiet ut.</p>
  </article>
  <article class="abs col" style="left:586px;top:530px">
    <h2>Why hire us?</h2>
    <div class="photo" role="img" aria-label="Installer fitting a satellite dish to a brick house wall" style="background:linear-gradient(135deg,#8c6a5a,#b89a88 50%,#3a3f4a)"></div>
    <p>Lorem ipsum dolor sit amet, consectetur adipiscing elit. Etiam tristique tristique lacus in varius. Donec nec vestibulum ligula. Aenean turpis diam, feugiat a luctus in, rhoncus eget risus. Maecenas consequat porttitor dui, vitae consequat massa imperdiet ut. Donec laoreet, elit ut tempus lobortis, eros leo molestie velit, non egestas augue nulla eget erat.</p>
  </article>
  <span class="btn" style="left:37px">READ MORE</span>
  <span class="btn" style="left:380px">READ MORE</span>
  <span class="btn" style="left:586px">READ MORE</span>
</main>

<footer class="abs footer">
  <div class="abs" style="left:38px;top:30px"><h3>Browse Site</h3>
    <ul style="margin-top:18px"><li>About our company</li><li>Contact us</li><li>Our</li><li>Our Prices</li><li>Online quote form</li><li>Client Testimonials</li></ul></div>
  <div class="abs" style="left:241px;top:31px"><h3>Our Testimonials</h3>
    <p class="testimonial" style="margin-top:17px">Lorem ipsum dolor sit amet, consectetur adipiscing elit. Etiam tristique tristique lacus in varius. Donec nec vestibulum ligula. Aenean turpis diam, feugiat a luctus in, rhoncus eget risus. Maecenas consequat porttitor dui, vitae consequat massa imperdiet ut. elit ut tempus lobortis, eros leo molestie velit.</p>
    <p class="testimonial" style="font-weight:700;color:#222">Dana R.</p></div>
  <div class="abs" style="left:573px;top:29px"><h3>From Our Blog</h3>
    <div class="post" style="margin-top:13px">April 1, 2016<a href="#">Lorem ipsum dolor sit amet, consectetur</a>adipiscing elit. Etiam tristique tristique lacus in varius. Donec nec vestibulum ligula. Aenean turpis diam...</div>
    <div class="post" style="margin-top:12px">April 1, 2016<a href="#">Lorem ipsum dolor sit amet, consectetur</a>adipiscing elit. Etiam tristique tristique lacus in varius. Donec nec vestibulum ligula. Aenean turpis diam...</div></div>
</footer>
<div class="abs bottom-bar"></div>
<div class="abs copyright">Copyright © 2016 Your&nbsp; Business. All rights reserved.</div>
<span class="abs social" style="left:752px;background:#4fa6d8"></span>
<span class="abs social" style="left:773px;background:#2a72b5"></span>
<span class="abs social" style="left:794px;background:#3b5a9a"></span>
</body>
</html>
```